Attractive door board for entrance beautysalon

Make an attractive design for a board that can be glued on the front door of a beauty salon. The salon location has no window in the front so I need something catchy and attractive. The door board contains a list of the services and the website: www.atelierkm.be, and the text "Enkel op afspraak, bel 0486317492"

Target Market(s)

woman between 16 and 99 years old

Industry/Entity Type

Beauty Salon

Font styles to use
Sans Serif

Requirements
Must have
• A very nice, attractive but sober design.
• It must have a classy Morvane, Lusa, ... chique design.
• The logo must be on it (in attachment)
• There must be the following list in it:
• Gelaatsverzorging
• Wimperverlenging
• Wimperlifting
• Suikerontharing
• Permanente Make Up
• Airbrush Tanning
• Manicure - Pedicure - Velura
• and then the website www.atelierkm.be, and the text "Enkel op afspraak, bel 0486317492"
Nice to have
• a catchy design,
• max. width can be 75 cm and max height 180 cm as it is a design for a board that will be glued on a door.
Should not have
• orchid flowers, buddha look a likes

```html
<!DOCTYPE html>
<html lang="nl">
<head>
<meta charset="utf-8">
<title>Atelier KM – deurbord</title>
<link rel="stylesheet" href="https://fonts.googleapis.com/css2?family=Questrial&family=Open+Sans:wght@400&display=swap">
<style>
  :root {
    --bg: #2b2c2d;
    --stripe-light: #353637;
    --stripe-dark: #232425;
    --panel: #141414;
    --text: #ffffff;
  }
  html, body {
    margin: 0;
    padding: 0;
    width: 1200px;
    height: 2877px;
    overflow: hidden;
    background: var(--bg);
  }
  .board {
    position: relative;
    width: 1200px;
    height: 2877px;
    overflow: hidden;
    background: var(--bg);
    color: var(--text);
  }
  .board__stripes {
    position: absolute;
    inset: 0;
  }
  .board__panel {
    position: absolute;
    left: 179px;
    top: 0;
    width: 837px;
    height: 2877px;
    background: var(--panel);
  }
  .brand__mark {
    position: absolute;
    left: 497px;
    top: 180px;
    width: 200px;
    height: 200px;
  }
  .brand__name {
    position: absolute;
    left: 244px;
    top: 488px;
    width: 714px;
    display: flex;
    justify-content: space-between;
    font-family: "Questrial", sans-serif;
    font-size: 64px;
    line-height: 64px;
  }
  .brand__gap { width: 40px; }
  .brand__tagline {
    position: absolute;
    left: 240px;
    top: 590px;
    width: 722px;
    text-align: center;
    font-family: "Questrial", sans-serif;
    font-size: 17px;
    line-height: 20px;
    letter-spacing: 24.5px;
    padding-left: 24.5px;
    box-sizing: border-box;
    white-space: nowrap;
  }
  .services {
    position: absolute;
    left: 182px;
    top: 1000px;
    margin: 0;
    padding: 0;
    list-style: none;
    font-family: "Questrial", sans-serif;
    font-size: 70px;
    line-height: 100px;
  }
  .services__item {
    position: relative;
    padding-left: 48px;
    margin-bottom: 100px;
    white-space: nowrap;
  }
  .services__item::before {
    content: "•";
    position: absolute;
    left: 0;
  }
  .services__item:last-child { margin-bottom: 0; }
  .contact {
    position: absolute;
    left: 0;
    width: 1194px;
    text-align: center;
    font-family: "Open Sans", sans-serif;
    white-space: nowrap;
  }
  .contact--web {
    top: 2398px;
    font-size: 104px;
    line-height: 116px;
  }
  .contact--call {
    top: 2597px;
    font-size: 68px;
    line-height: 89px;
  }
</style>
</head>
<body>
<main class="board">
  <svg class="board__stripes" width="1200" height="2877" viewBox="0 0 1200 2877" aria-hidden="true">
    <polygon points="0,600 1200,-300 1200,0 0,900" fill="var(--stripe-light)"/>
    <polygon points="0,1200 1200,300 1200,500 0,1400" fill="var(--stripe-dark)"/>
    <polygon points="0,1800 1200,900 1200,1250 0,2150" fill="var(--stripe-light)"/>
    <polygon points="0,2450 1200,1550 1200,1750 0,2650" fill="var(--stripe-dark)"/>
    <polygon points="0,3050 1200,2150 1200,2500 0,3400" fill="var(--stripe-light)"/>
  </svg>
  <div class="board__panel"></div>

  <svg class="brand__mark" width="200" height="200" viewBox="0 0 200 200" aria-hidden="true">
    <circle cx="100" cy="100" r="96" fill="none" stroke="var(--text)" stroke-width="4"/>
  </svg>
  <div class="brand__name" aria-label="Atelier KM">
    <span>A</span><span>T</span><span>E</span><span>L</span><span>I</span><span>E</span><span>R</span><span class="brand__gap"></span><span>K</span><span>M</span>
  </div>
  <div class="brand__tagline">SCHOONHEIDSINSTITUUT</div>

  <ul class="services">
    <li class="services__item">Gelaatsverzorging</li>
    <li class="services__item">Wimperverlenging</li>
    <li class="services__item">Suikerontharing</li>
    <li class="services__item">Permanente Make Up</li>
    <li class="services__item">Airbrush Tanning</li>
    <li class="services__item">Manicure - Pedicure<br>- Velura</li>
  </ul>

  <div class="contact contact--web">www.atelierkm.be</div>
  <div class="contact contact--call">Enkel op afspraak,<br>bel 0486317492</div>
</main>
</body>
</html>
```